Business Book - Quiet Mornings at the Ledger Desk (Finding Calm Among Daily Numbers)

I'm looking for a cover that appeals to successful business people who are used to reading business titles.

The cover should feel familiar and fit in with the existing canon of bestselling business books with a vibrant, but professional look (see attached).

I want my book to stand out, but not to be frivolous. Abstract is probably best. Or close to it.

Please feel free to use my brand colours, or go with something else -

Teal
HEX #199BAB
25 / 155 / 171

Coral
HEX #EE786E
238 / 120/ 110

I don't want to include anything connected with robots or gendered assistants/business people. Or headsets.

It's only 24 hours which is mental

```html
<!DOCTYPE html>
<html lang="en">
<head>
<meta charset="utf-8">
<title>Quiet Mornings at the Ledger Desk — Cover</title>
<link rel="stylesheet" href="https://fonts.googleapis.com/css2?family=Montserrat:wght@300;400&display=swap">
<style>
  :root {
    --ink: #000000;
    --deep-navy: #02121c;
    --glow-teal: #0d5a80;
    --glow-haze: rgba(150, 190, 205, 0.35);
    --sphere-light: #7fe9f5;
    --sphere-mid: #1e9af0;
    --sphere-deep: #0a3d78;
    --sphere-shadow: #020a14;
    --title: #ffffff;
  }
  * { margin: 0; padding: 0; box-sizing: border-box; }
  html, body {
    width: 848px;
    height: 1200px;
    overflow: hidden;
    background: var(--ink);
  }
  .cover {
    position: relative;
    width: 848px;
    height: 1200px;
    overflow: hidden;
    background:
      radial-gradient(ellipse 150px 40px at 140px 25px, var(--glow-haze), transparent 70%),
      radial-gradient(ellipse 520px 620px at 0 60px, var(--glow-teal) 0%, rgba(5, 40, 60, 0.7) 35%, transparent 75%),
      linear-gradient(135deg, var(--deep-navy) 0%, var(--ink) 55%);
  }
  .cover__sphere {
    position: absolute;
    left: 31px;
    top: 205px;
    width: 786px;
    height: 786px;
  }
  .cover__title {
    position: absolute;
    right: 33px;
    top: 812px;
    width: 300px;
    text-align: right;
    font-family: "Montserrat", sans-serif;
    font-weight: 300;
    font-size: 36px;
    line-height: 44px;
    letter-spacing: 0.2px;
    color: var(--title);
  }
  .cover__title span { display: block; }
</style>
</head>
<body>
  <main class="cover">
    <svg class="cover__sphere" viewBox="0 0 786 786" role="img" aria-label="Abstract sphere formed by glowing blue spiralling lines and dotted arcs">
      <defs>
        <radialGradient id="sphere-fill" cx="0.42" cy="0.3" r="0.75">
          <stop offset="0" stop-color="var(--sphere-light)" stop-opacity="0.55"/>
          <stop offset="0.35" stop-color="var(--sphere-mid)" stop-opacity="0.45"/>
          <stop offset="0.7" stop-color="var(--sphere-deep)" stop-opacity="0.4"/>
          <stop offset="1" stop-color="var(--sphere-shadow)" stop-opacity="0.6"/>
        </radialGradient>
      </defs>
      <circle cx="393" cy="393" r="392" fill="url(#sphere-fill)"/>
    </svg>

    <h1 class="cover__title">
      <span>Quiet</span>
      <span>Mornings at</span>
      <span>the Ledger</span>
      <span>Desk</span>
    </h1>
  </main>
</body>
</html>
```